Quenderil - Still Grace Cosmetics

Please design a logo and business cards for new food supplements, cosmetics and herbal fixatives. The products are produced ecologically and biologically in the South Tyrol and Trentino alps. The products are pure and noble. Quenderil = pure vitality Colors Background: dark or black matt (soft touch) Logodesign: powerful, elegant, violet with glossy foil The logo and design should convey warmth, passion and the 6th sense, you should get the impression that you can smell the herbal odor , Logo and business cards for new food supplements, cosmetics and herbal fixatives. The products are produced ecologically and biologically in the South Tyrol and Trentino alps. The products are pure and noble. Quenderil = pure vitality Colors Background: dark or black matt (softtouch) Logodesign: powerful elegant violet with glossy foil The logo and design is meant to convey warmth, passion and the 6th sense, you should get the impression that you can smell the herbal perfume.

Target Market(s)

Food, food supplements, vitality, health

Contact Information for Business Card

Please provide an elegant darf design that is puristic, but has a very good logo design
Elegantes dunkles design, puristisch

Logo Text

Quenderil - still Grace

Colors
6b449b

Requirements
Must have
• SVG Files Alpha channel for foil embossing High-quality design
Nice to have
• Pure elegance
Should not have
• to colorful colors

```html
<!DOCTYPE html>
<html lang="en">
<head>
<meta charset="utf-8">
<title>Quenderil – Business Cards</title>
<link href="https://fonts.googleapis.com/css2?family=Questrial&family=Work+Sans:wght@400;500&display=swap" rel="stylesheet">
<style>
  :root {
    --stage: #1b1b1d;
    --card-dark: #3d3d3f;
    --card-light: #ffffff;
    --violet: #6b449b;
    --ink: #3a3a3c;
    --text-light: #f2f2f2;
    --text-soft: #d6d6d8;
  }
  * { box-sizing: border-box; margin: 0; padding: 0; }
  html, body {
    width: 1200px; height: 852px; overflow: hidden;
    background: var(--stage);
  }
  .stage {
    width: 1200px; height: 852px;
    display: flex; flex-direction: column;
    align-items: center; justify-content: center; gap: 44px;
  }
  .card {
    position: relative;
    width: 580px; height: 332px;
    border-radius: 16px;
    overflow: hidden;
    box-shadow: 0 14px 34px rgba(0,0,0,0.55);
  }
  .card--back {
    background: var(--card-dark);
    display: flex; align-items: center; justify-content: center;
  }
  .brand-name {
    font-family: "Questrial", sans-serif;
    font-weight: 400;
    letter-spacing: 1px;
  }
  .card--back .brand-name { color: var(--text-light); font-size: 64px; }
  .card--front { background: var(--card-light); }
  .card-shape { position: absolute; inset: 0; width: 100%; height: 100%; }
  .card--front .brand-name {
    position: absolute; left: 40px; top: 52px;
    color: var(--ink); font-size: 36px; line-height: 1.2;
  }
  .holder {
    position: absolute; right: 34px; top: 136px;
    text-align: right; color: var(--text-light);
    font-family: "Work Sans", sans-serif;
  }
  .holder-name { font-size: 19px; font-weight: 500; letter-spacing: 1px; }
  .holder-role { font-size: 12px; color: var(--text-soft); margin-top: 2px; }
  .holder-address { font-size: 12.5px; color: var(--text-soft); margin-top: 18px; line-height: 1.45; }
  .contacts {
    position: absolute; left: 40px; bottom: 24px;
    list-style: none;
    font-family: "Work Sans", sans-serif;
    font-size: 13px; color: var(--text-light);
  }
  .contacts li { display: flex; align-items: center; gap: 10px; line-height: 21px; }
  .contacts svg { width: 10px; height: 10px; fill: none; stroke: var(--text-soft); stroke-width: 1.4; }
  .contacts strong { font-weight: 500; }
</style>
</head>
<body>
<main class="stage">
  <section class="card card--back" aria-label="Card back">
    <span class="brand-name">Quenderil</span>
  </section>

  <section class="card card--front" aria-label="Card front">
    <svg class="card-shape" viewBox="0 0 580 332" preserveAspectRatio="none" aria-hidden="true">
      <path d="M0,196 Q160,86 580,62 L580,88 Q165,100 0,212 Z" fill="var(--violet)"/>
      <path d="M0,222 Q170,110 580,96 L580,332 L0,332 Z" fill="var(--card-dark)"/>
    </svg>

    <span class="brand-name">Quenderil</span>

    <div class="holder">
      <p class="holder-name">LUKAS FERRAN</p>
      <p class="holder-role">Managing Partner</p>
      <p class="holder-address">Talweg 14, 39012<br>Meran, Italy</p>
    </div>

    <ul class="contacts">
      <li>
        <svg viewBox="0 0 10 10"><path d="M2,1 L4,1 L4.5,3 L3.3,4 Q4.5,6 6,6.7 L7,5.5 L9,6 L9,8 Q5,9.5 1,3 Z"/></svg>
        <span>+49 170 482 306 17</span>
      </li>
      <li>
        <svg viewBox="0 0 10 10"><rect x="1" y="2" width="8" height="6"/><path d="M1,2 L5,5.5 L9,2"/></svg>
        <span>info@quenderil.com</span>
      </li>
      <li>
        <svg viewBox="0 0 10 10"><circle cx="5" cy="5" r="4"/><path d="M1,5 H9 M5,1 Q2.5,5 5,9 M5,1 Q7.5,5 5,9"/></svg>
        <span>www.<strong>quenderil</strong>.com</span>
      </li>
    </ul>
  </section>
</main>
</body>
</html>
```